Redesign www.KORVADA.ch - Shoplane Web-Shop - Storytelling

Redesign of existing Shoplane Web-page of KOR-VADA.ch.
Please carefully review both enclosed documents. The annotated notes explain the expected design direction and priorities.

```html
<!DOCTYPE html>
<html lang="en">
<head>
<meta charset="utf-8">
<title>KOR-VADA – Swiss Handmade Scarves</title>
<link href="https://fonts.googleapis.com/css2?family=Barlow+Condensed:wght@600;700&family=Outfit:wght@300;400;500;600&display=swap" rel="stylesheet">
<style>
:root{
  --slate:#4b5159;
  --ink:#3c4148;
  --text:#4a4f56;
  --muted:#6d7278;
  --sand:#f3f1ed;
  --white:#ffffff;
  --line:#d9d9d9;
  --star:#f0a21a;
}
*{box-sizing:border-box;margin:0;padding:0}
html,body{width:1200px;height:3795px;overflow:hidden;background:var(--white)}
body{position:relative;font-family:"Outfit",sans-serif;color:var(--text)}
.abs{position:absolute}
.display{font-family:"Barlow Condensed",sans-serif;font-weight:700;color:var(--slate);text-transform:uppercase;letter-spacing:.5px}
.btn{position:absolute;display:flex;align-items:center;justify-content:center;background:var(--slate);color:var(--white);font-size:12px;font-weight:500;text-transform:uppercase;letter-spacing:.3px}

/* header */
.site-header{left:0;top:0;width:1200px;height:86px;background:var(--white)}
.menu-toggle{left:113px;top:21px;width:45px;height:44px;background:var(--sand);display:flex;align-items:center;justify-content:center}
.menu-label{left:166px;top:33px;font-family:"Barlow Condensed",sans-serif;font-weight:700;font-size:16px;color:var(--ink)}
.brand{left:520px;top:30px;width:160px;display:flex;align-items:center;justify-content:center;gap:8px;font-family:"Outfit",sans-serif;font-weight:600;font-size:22px;color:var(--slate)}
.brand-square{width:12px;height:12px;background:var(--slate)}
.header-icons{left:990px;top:32px;display:flex;gap:18px}

/* hero */
.hero{left:0;top:86px;width:1200px;height:615px;background:var(--sand)}
.hero-title{left:116px;top:236px;font-size:62px;line-height:60px;width:440px}
.hero-text{left:116px;top:420px;width:380px;font-size:13px;line-height:19px;color:var(--text)}
.hero-btn{left:116px;top:473px;width:170px;height:42px}
.hero-photo{left:600px;top:140px;width:500px;height:561px;background:linear-gradient(120deg,#d9d4cb 0%,#e8ddd0 45%,#c9ccd2 100%)}

/* features */
.feature{top:776px;width:200px;text-align:center}
.feature-icon{width:54px;height:54px;margin:0 auto;background:var(--slate);display:flex;align-items:center;justify-content:center}
.feature p{margin-top:13px;font-size:13px;line-height:19px;color:var(--ink)}

/* story */
.story-frame{left:196px;top:989px;width:359px;height:332px;border:1.5px solid var(--ink)}
.story-photo{left:208px;top:967px;width:369px;height:342px;background:linear-gradient(160deg,#55575c,#3f4045)}
.story-title{left:630px;top:1024px;font-size:42px;line-height:45px}
.story-text{left:630px;top:1122px;width:390px;font-size:13px;line-height:19px;color:var(--text)}
.story-btn{left:630px;top:1216px;width:143px;height:42px}

/* products */
.products{left:0;top:1412px;width:1200px;height:620px;background:var(--sand)}
.section-title{left:0;width:1200px;text-align:center;font-size:42px;line-height:46px}
.product{top:1542px;width:210px;text-align:center}
.product-photo{width:210px;height:250px;background:var(--white);display:flex;align-items:center;justify-content:center}
.product-photo span{width:110px;height:200px;border-radius:40px 40px 8px 8px}
.product-name{margin-top:16px;font-size:13px;line-height:19px;color:var(--text)}
.product-price{font-size:13px;font-weight:600;color:var(--ink);margin-top:2px}
.product-cart{font-size:11px;font-weight:500;text-decoration:underline;margin-top:4px;color:var(--ink)}
.show-all{left:540px;top:1927px;width:120px;height:43px}

/* values */
.values-panel{left:134px;top:2189px;width:704px;height:448px;background:var(--sand)}
.values-photo{left:599px;top:2130px;width:466px;height:450px;background:linear-gradient(135deg,#e9d5cc 0%,#d9aea3 50%,#efeae6 100%)}
.value{width:210px;text-align:center}
.value h3{font-size:15px;font-weight:500;color:var(--ink);margin-top:6px}
.value p{font-size:13px;line-height:19px;color:var(--muted);margin-top:4px}

/* testimonials */
.review{top:2789px;width:302px;height:204px;background:var(--white);box-shadow:0 2px 14px rgba(0,0,0,.09);padding:20px 16px}
.review-head{display:flex;align-items:center;gap:10px}
.avatar{width:68px;height:68px;border-radius:50%;flex:none}
.review-name{font-size:15px;font-weight:500;color:var(--ink)}
.review-date{font-size:10px;color:var(--muted)}
.stars{margin-left:auto;color:var(--star);font-size:13px;letter-spacing:2px;align-self:flex-start;margin-top:16px}
.review p{margin-top:14px;font-size:11.5px;line-height:19px;color:var(--text)}

/* community */
.community-title{top:3078px;font-size:52px;line-height:54px}
.community-text{left:0;top:3138px;width:1200px;text-align:center;font-size:13px;line-height:19px;color:var(--text)}
.signup{left:402px;top:3201px;width:396px;height:38px;border:1.5px solid var(--ink);display:flex;align-items:center;justify-content:space-between;padding:0 18px;font-size:11px;color:var(--muted)}

/* footer */
.site-footer{left:0;top:3345px;width:1200px;height:450px;background:var(--slate);color:var(--white)}
.footer-brand{left:500px;top:3444px;width:200px;display:flex;align-items:center;justify-content:center;gap:10px;font-family:"Outfit",sans-serif;font-weight:600;font-size:26px;color:var(--white)}
.footer-brand .brand-square{background:var(--white);width:14px;height:14px}
.footer-title{left:0;top:3532px;width:1200px;text-align:center;font-size:50px;line-height:54px;color:var(--white)}
.footer-btn{left:503px;top:3599px;width:192px;height:38px;background:var(--white);color:var(--slate)}
.footer-links{left:134px;top:3670px;width:932px;display:flex;justify-content:space-between;font-size:13px;color:var(--white)}
.footer-rule{left:112px;top:3741px;width:975px;height:1px;background:#6b7078}
.copyright{left:0;top:3758px;width:1200px;text-align:center;font-size:12px;color:var(--white)}
</style>
</head>
<body>

<header class="abs site-header">
  <div class="abs menu-toggle">
    <svg width="20" height="14" viewBox="0 0 20 14"><path d="M0 1h20M0 7h14M0 13h20" stroke="#3c4148" stroke-width="1.6"/></svg>
  </div>
  <div class="abs menu-label">MENU</div>
  <div class="abs brand"><span class="brand-square"></span>KOR-VADA</div>
  <div class="abs header-icons">
    <svg width="18" height="18" viewBox="0 0 18 18"><circle cx="7.5" cy="7.5" r="5.5" fill="none" stroke="#3c4148" stroke-width="1.5"/><path d="M11.5 11.5L16 16" stroke="#3c4148" stroke-width="1.5"/></svg>
    <svg width="22" height="20" viewBox="0 0 22 20"><path d="M3 6h12l-1 11H4z" fill="none" stroke="#3c4148" stroke-width="1.5"/><path d="M6 6a3 3 0 016 0" fill="none" stroke="#3c4148" stroke-width="1.5"/><circle cx="16" cy="15" r="4.5" fill="#e0393e"/></svg>
    <svg width="20" height="18" viewBox="0 0 20 18"><path d="M10 16.5S1.5 11 1.5 5.5A4 4 0 0110 3.5a4 4 0 018.5 2C18.5 11 10 16.5 10 16.5z" fill="none" stroke="#3c4148" stroke-width="1.5"/></svg>
  </div>
</header>

<section class="abs hero">
</section>
<h1 class="abs display hero-title">Handmade unique pieces for women with style.</h1>
<p class="abs hero-text">Each KOR-VADA scarf is one of a kind carefully crafted to add personality to your outfit.</p>
<div class="btn hero-btn">Discover scarves</div>
<div class="abs hero-photo" role="img" aria-label="Two mannequins wearing a denim jacket and a knit top, each styled with a colourful silk scarf"></div>

<section>
  <div class="abs feature" style="left:180px">
    <div class="feature-icon"><svg width="26" height="26" viewBox="0 0 26 26"><path d="M8 3v20M13 3v20M18 3v20M3 8h20M3 13h20M3 18h20" stroke="#fff" stroke-width="1.2"/></svg></div>
    <p>High-quality fabrics without<br>scratching</p>
  </div>
  <div class="abs feature" style="left:393px">
    <div class="feature-icon"><svg width="26" height="26" viewBox="0 0 26 26"><text x="13" y="19" text-anchor="middle" fill="#fff" font-family="Outfit,sans-serif" font-size="17">⅓</text></svg></div>
    <p>Only 1-3 pieces per<br>design</p>
  </div>
  <div class="abs feature" style="left:607px">
    <div class="feature-icon"><svg width="26" height="26" viewBox="0 0 26 26"><path d="M6 15l6-9a2 2 0 013 2l-2 3 5-4a2 2 0 012 3l-5 4 4-2a2 2 0 011 3l-7 5a6 6 0 01-8-1z" fill="none" stroke="#fff" stroke-width="1.3"/></svg></div>
    <p>Handmade locally in<br>Switzerland</p>
  </div>
  <div class="abs feature" style="left:819px">
    <div class="feature-icon"><svg width="26" height="26" viewBox="0 0 26 26"><path d="M21 4C12 5 7 11 6 20M6 20c6-1 12-5 15-16M10 14h6M3 22h12" fill="none" stroke="#fff" stroke-width="1.3"/></svg></div>
    <p>Lightweight and suitable<br>for everyday use</p>
  </div>
</section>

<section>
  <div class="abs story-frame"></div>
  <div class="abs story-photo" role="img" aria-label="Portrait of the designer wearing a leather jacket and a patterned scarf"></div>
  <h2 class="abs display story-title">KOR-VADA<br>Story Designer</h2>
  <p class="abs story-text">Fabrics have been part of my life since childhood.<br>My grandmother and my mother created with their hands and this is exactly what I continue today. I consciously take my time for each piece...</p>
  <div class="btn story-btn">View new pieces</div>
</section>

<section class="abs products"></section>
<h2 class="abs display section-title" style="top:1474px">Product teaser</h2>
<div class="abs product" style="left:152px">
  <div class="product-photo"><span role="img" aria-label="Scarf on a mannequin with an ombre denim blouse" style="background:linear-gradient(#c9a9a6,#4e6a8c)"></span></div>
  <div class="product-name">Liora Triangular Scarf<br>Small Scarf</div><div class="product-price">CHF 39.00</div><div class="product-cart">ADD TO CART</div>
</div>
<div class="abs product" style="left:380px">
  <div class="product-photo"><span role="img" aria-label="Checked scarf on a mannequin with a red cardigan" style="background:linear-gradient(#3d4f86,#d42a4a)"></span></div>
  <div class="product-name">Liora Triangular Scarf<br>Small Scarf</div><div class="product-price">CHF 39.00</div><div class="product-cart">ADD TO CART</div>
</div>
<div class="abs product" style="left:609px">
  <div class="product-photo"><span role="img" aria-label="Blue gingham scarf on a mannequin with a denim shirt" style="background:linear-gradient(#6c8fc8,#2e7fb8)"></span></div>
  <div class="product-name">Liora Triangular Scarf<br>Small Scarf</div><div class="product-price">CHF 39.00</div><div class="product-cart">ADD TO CART</div>
</div>
<div class="abs product" style="left:838px">
  <div class="product-photo"><span role="img" aria-label="Brown dotted scarf on a mannequin with a blue shirt" style="background:linear-gradient(#7a4a3e,#3e5874)"></span></div>
  <div class="product-name">Liora Triangular Scarf<br>Small Scarf</div><div class="product-price">CHF 39.00</div><div class="product-cart">ADD TO CART</div>
</div>
<div class="btn show-all">Show all</div>

<section>
  <div class="abs values-panel"></div>
  <div class="abs values-photo" role="img" aria-label="Soft pink fringed scarf draped over a white blouse beside a magazine and flowers"></div>
  <div class="abs value" style="left:159px;top:2240px">
    <svg width="28" height="30" viewBox="0 0 28 30"><path d="M6 2h12l6 6v20H6z M18 2v6h6 M10 14h10M10 18h10M10 22h7" fill="none" stroke="#4b5159" stroke-width="1.3"/></svg>
    <h3>Story - Creation</h3>
    <p>Each scarf begins with carefully<br>selected fabrics.</p>
  </div>
  <div class="abs value" style="left:368px;top:2346px">
    <svg width="30" height="30" viewBox="0 0 30 30"><circle cx="15" cy="15" r="13" fill="none" stroke="#4b5159" stroke-width="1.3"/><rect x="9" y="9" width="12" height="12" fill="none" stroke="#4b5159" stroke-width="1.2"/><path d="M9 13h12M13 9v12M17 9v12" stroke="#4b5159" stroke-width="1"/></svg>
    <h3>Usage / Everyday</h3>
    <p>Whether in everyday life, at the<br>office or on a walk.</p>
  </div>
  <div class="abs value" style="left:159px;top:2454px">
    <svg width="28" height="30" viewBox="0 0 28 30"><circle cx="14" cy="12" r="9" fill="none" stroke="#4b5159" stroke-width="1.3"/><path d="M10 24h8M11 27h6M14 7l1.5 3 3 .4-2.2 2 .6 3-2.9-1.5-2.9 1.5.6-3-2.2-2 3-.4z" fill="none" stroke="#4b5159" stroke-width="1.1"/></svg>
    <h3>Uniqueness</h3>
    <p>Only 1 to 3 scarves are made<br>from each fabric.</p>
  </div>
</section>

<section>
  <h2 class="abs display section-title" style="top:2720px">Our testimonials</h2>
  <article class="abs review" style="left:130px">
    <div class="review-head"><div class="avatar" role="img" aria-label="Customer portrait" style="background:linear-gradient(#d7868e,#e9c9b4)"></div><div><div class="review-name">Renata</div><div class="review-date">1 year ago</div></div><div class="stars">★★★★★</div></div>
    <p>Hi, Marlena just sewed me two absolutely gorgeous rain hats..in my favorite colors, lilac and pink. They're not only incredibly beautiful, but also unbelievably comfortable...</p>
  </article>
  <article class="abs review" style="left:449px">
    <div class="review-head"><div class="avatar" role="img" aria-label="Customer portrait" style="background:linear-gradient(#8ea4b8,#2e9fa4)"></div><div><div class="review-name">Corinne</div><div class="review-date">2 year ago</div></div><div class="stars">★★★★★</div></div>
    <p>I'm a huge fan of KOR-VADA and already own countless gorgeous scarves from Marlena. The quality is always top-notch and the craftsmanship is perfect. I'm already looking...</p>
  </article>
  <article class="abs review" style="left:769px">
    <div class="review-head"><div class="avatar" role="img" aria-label="Customer portrait" style="background:linear-gradient(#8c3a2a,#2aa0a8)"></div><div><div class="review-name">Helga</div><div class="review-date">1 year ago</div></div><div class="stars">★★★★★</div></div>
    <p>I already own countless scarves &amp; hats from KOR-VADA and I'm thrilled with them. I simply can't resist their fantastic designs. The fabrics are always so beautiful, &amp; the quality...</p>
  </article>
</section>

<section>
  <h2 class="abs display section-title community-title">Join the community</h2>
  <p class="abs community-text">Find out when new models are released and where you can meet KOR-VADA in person.<br>I also share tips on how to wear the scarves.</p>
  <div class="abs signup"><span>Enter Your Email Address...</span>
    <svg width="14" height="14" viewBox="0 0 14 14"><path d="M1 6.5L13 1 9 13 7 8z" fill="#3c4148"/></svg>
  </div>
</section>

<footer class="abs site-footer"></footer>
<div class="abs footer-brand"><span class="brand-square"></span>KOR-VADA</div>
<h2 class="abs display footer-title">Discover your unique piece</h2>
<div class="btn footer-btn">Discover scarves now</div>
<nav class="abs footer-links">
  <span>Seek</span><span>General terms and conditions of business</span><span>Data protection</span><span>imprint</span><span>Shipping conditions</span><span>Refunds</span><span>Privacy settings</span>
</nav>
<div class="abs footer-rule"></div>
<div class="abs copyright">2028, KOR-VADA Powered by Shoplane</div>

</body>
</html>
```